Business Card Design

We need a business card for a new furniture company in Utah. We are introducing a fresh new concept in Utah and would like a card to reflect to buyers that they can buy quality furniture and get it NOW. I am open to just about any color scheme, but I would like something that pops.

Industry/Entity Type

Business

Contact Information for Business Card

Sofa Haven, Glen Marsh
41 S. Pine Hollow Lane
Cedar Brook Utah 84217

```html
<!DOCTYPE html>
<html lang="en">
<head>
<meta charset="utf-8">
<title>Sofa Haven — Business Card</title>
<link href="https://fonts.googleapis.com/css2?family=Arimo:wght@400;700&display=swap" rel="stylesheet">
<style>
  :root {
    --slate: #393848;
    --orange: #f2733f;
    --paper: #ffffff;
    --backdrop: #d9d9dc;
    --ink: #2c2b36;
    --muted: #4a4958;
  }
  html, body {
    margin: 0;
    width: 1200px;
    height: 1200px;
    overflow: hidden;
    background: var(--backdrop);
    font-family: "Arimo", Arial, sans-serif;
  }
  .card {
    position: absolute;
    left: 100px;
    top: 310px;
    width: 1000px;
    height: 580px;
    background: var(--paper);
    box-shadow: 0 10px 30px rgba(0,0,0,0.18);
  }
  .brand-band {
    position: absolute;
    left: 14px;
    top: 14px;
    right: 14px;
    height: 226px;
    background: var(--slate);
    display: flex;
    align-items: flex-end;
    padding: 0 0 36px 250px;
    box-sizing: border-box;
    gap: 30px;
  }
  .brand-mark {
    width: 84px;
    height: 84px;
    border-radius: 50%;
    border: 1.5px solid #5a596a;
    box-sizing: border-box;
    flex: none;
    margin-bottom: -22px;
  }
  .brand-name {
    color: var(--paper);
    font-size: 58px;
    font-weight: 400;
    letter-spacing: 4px;
    line-height: 1;
  }
  .person {
    position: absolute;
    left: 430px;
    top: 262px;
  }
  .person-name {
    font-size: 36px;
    font-weight: 700;
    color: var(--ink);
    margin: 0;
  }
  .person-title {
    font-size: 22px;
    color: var(--muted);
    margin: 4px 0 0 56px;
  }
  .divider {
    position: absolute;
    left: 598px;
    top: 340px;
    width: 2px;
    height: 60px;
    background: var(--orange);
  }
  .address {
    position: absolute;
    left: 512px;
    top: 410px;
    font-size: 28px;
    line-height: 1.35;
    color: var(--muted);
    text-align: center;
    margin: 0;
    font-style: normal;
  }
  .accent-bar {
    position: absolute;
    left: 300px;
    right: 250px;
    top: 508px;
    height: 12px;
    background: var(--orange);
  }
  .base-strip {
    position: absolute;
    left: 0;
    right: 14px;
    bottom: 14px;
    height: 30px;
    background: var(--slate);
  }
</style>
</head>
<body>
  <div class="card">
    <header class="brand-band">
      <div class="brand-mark"></div>
      <div class="brand-name">Sofa Haven</div>
    </header>
    <div class="person">
      <p class="person-name">Glen Marsh</p>
      <p class="person-title">Manager</p>
    </div>
    <div class="divider"></div>
    <address class="address">41 S. Pine Hollow Lane<br>Cedar Brook Utah 84217</address>
    <div class="accent-bar"></div>
    <div class="base-strip"></div>
  </div>
</body>
</html>
```